Harbor-Glow

Letter heads, business cards, packaging envelopes big and small, and stationery
We have logo design and trademarked approval, we would lie to
upload design to help create this project.
This product was created for my Mother a 4 time diganosed Cancer
Survivor, This product has patent pending and now will be offered to the general public as well.
We are looking foward to working with all of you as this product
and stationary will be viewed worldwide.
Thanks
The Penwick Family

all ages and worldwide

Business

Must have
• Our Logo

```html
<!DOCTYPE html>
<html lang="en">
<head>
<meta charset="utf-8">
<title>Harbor-Glow Letterhead</title>
<link href="https://fonts.googleapis.com/css2?family=Arimo:wght@400;700&family=Ubuntu:wght@700&display=swap" rel="stylesheet">
<style>
  :root {
    --navy: #1c3966;
    --red: #c0202d;
    --paper: #ffffff;
    --ground: #e9e6e1;
    --faint: #f0f0f1;
    --ink-light: #ffffff;
  }
  html, body {
    margin: 0;
    padding: 0;
    width: 1053px;
    height: 1200px;
    overflow: hidden;
    background: var(--ground);
  }
  .letterhead {
    position: absolute;
    left: 101px;
    top: 50px;
    width: 850px;
    height: 1100px;
    background: var(--paper);
    overflow: hidden;
    box-shadow: 0 2px 8px rgba(0,0,0,0.12);
  }
  .brand {
    position: absolute;
    top: 52px;
    left: 0;
    width: 100%;
    display: flex;
    justify-content: center;
  }
  .brand-row {
    display: flex;
    align-items: center;
    gap: 12px;
  }
  .brand-dot {
    width: 30px;
    height: 30px;
    border-radius: 50%;
    background: var(--red);
  }
  .brand-name {
    font-family: "Ubuntu", "Arimo", sans-serif;
    font-weight: 700;
    font-size: 42px;
    color: var(--navy);
    letter-spacing: -0.5px;
    line-height: 1;
  }
  .backdrop-name {
    position: absolute;
    top: 420px;
    left: 0;
    width: 100%;
    text-align: center;
    font-family: "Ubuntu", "Arimo", sans-serif;
    font-weight: 700;
    font-size: 120px;
    color: var(--faint);
    letter-spacing: -2px;
  }
  .footer-rule {
    position: absolute;
    left: 0;
    width: 100%;
    top: 1010px;
    height: 5px;
    background: var(--red);
  }
  .footer-band {
    position: absolute;
    left: 0;
    width: 100%;
    top: 1022px;
    height: 78px;
    background: var(--navy);
  }
  .contact {
    position: absolute;
    font-family: "Arimo", Arial, sans-serif;
    font-size: 14px;
    color: var(--ink-light);
    line-height: 19px;
  }
  .contact-address { left: 94px; top: 1061px; }
  .contact-phones { left: 468px; top: 1042px; }
  .contact-online { left: 630px; top: 1042px; }
  .contact-line {
    display: flex;
    align-items: center;
    gap: 5px;
  }
  .contact-line svg { width: 12px; height: 12px; }
</style>
</head>
<body>
  <main class="letterhead">
    <header class="brand">
      <div class="brand-row">
        <span class="brand-dot"></span>
        <span class="brand-name">Harbor-Glow</span>
      </div>
    </header>

    <div class="backdrop-name" aria-hidden="true">Harbor-Glow</div>

    <div class="footer-rule" aria-hidden="true"></div>
    <div class="footer-band" aria-hidden="true"></div>

    <div class="contact contact-address">Street Name, City, State, zip code</div>

    <div class="contact contact-phones">
      <div class="contact-line">
        <svg viewBox="0 0 12 12"><circle cx="6" cy="6" r="5.3" fill="none" stroke="#fff" stroke-width="1"/><path d="M4,3 L5,3 L5.6,4.6 L4.9,5.2 C5.3,6.2 5.8,6.7 6.8,7.1 L7.4,6.4 L9,7 L9,8 C6,8.6 3.4,6 4,3 Z" fill="#fff"/></svg>
        <span>123-456-7890</span>
      </div>
      <div class="contact-line">
        <svg viewBox="0 0 12 12"><rect x="3" y="1" width="5" height="4" fill="#fff"/><rect x="1" y="5" width="10" height="6" rx="1" fill="#fff"/></svg>
        <span>123-456-7890</span>
      </div>
    </div>

    <div class="contact contact-online">
      <div class="contact-line">
        <svg viewBox="0 0 12 12"><rect x="1" y="3" width="10" height="7" fill="#fff"/><path d="M1,3 L6,7 L11,3" fill="none" stroke="var(--navy)" stroke-width="1"/></svg>
        <span>hello@harborglow.net</span>
      </div>
      <div class="contact-line">
        <svg viewBox="0 0 12 12"><circle cx="6" cy="6" r="5" fill="none" stroke="#fff" stroke-width="1"/><ellipse cx="6" cy="6" rx="2.2" ry="5" fill="none" stroke="#fff" stroke-width="1"/><path d="M1,6 H11 M2,3.5 H10 M2,8.5 H10" stroke="#fff" stroke-width="0.8"/></svg>
        <span>www.harborglow.net</span>
      </div>
    </div>
  </main>
</body>
</html>
```